Professional Product Packaging Design

Hey Everyone,

We are looking for someone to help bring our vision and dreams to life. We have many details and ideas, along with templates already created. We simply need the graphic work completed.

We are a plant-based skin and body care company www.balmvesper.com, looking to improve our products branding and customer satisfaction through beautiful new packaging.

Thank you,

Rory

Target Market(s)

Health, Wellness, and Medical

Industry/Entity Type

Beauty

Colors
fff5ef

Requirements
Must have
• - Each product to have its own color scheme – View Labels attached
• - Natural – Modern – Youthful – On Trend
• -Logo
• -Balm Vesper
• -Plant Based Skin and Body Care
• -Ingredients – will be given
• -Size – 238ml/8fl.oz and 50ml/2fl.oz
• -Social Media- @balmvesper
• -Website – www.balmvesper.com
• - Organic, Non GMO, Vegan, Earth friendly
• -Description - will be given
• -Benefits – will be given
• - *Aroma*
• --UPC – will be given when needed
Nice to have
• Ingredient images

```html
<!DOCTYPE html>
<html lang="en">
<head>
<meta charset="utf-8">
<title>Balm Vesper – Muscle and Joint Packaging</title>
<link href="https://fonts.googleapis.com/css2?family=Bebas+Neue&family=Montserrat:wght@300;500;600;700&display=swap" rel="stylesheet">
<style>
  :root{
    --stage:#1e1e1e;
    --paper:#f7f7f6;
    --teal:#5cc4c9;
    --teal-deep:#3fb0b6;
    --red:#d8262c;
    --red-soft:#e4474b;
    --ink:#161616;
    --grey:#555;
    --badge:#c9cfc2;
  }
  *{box-sizing:border-box;margin:0;padding:0}
  html,body{width:1200px;height:1176px;overflow:hidden;background:var(--stage)}
  .canvas{position:relative;width:1200px;height:1176px}
  .panel{position:absolute;overflow:hidden;background:var(--paper)}
  .condensed{font-family:"Bebas Neue",sans-serif;font-weight:400}
  .sans{font-family:"Montserrat",sans-serif}

  .brand{text-align:center;color:var(--ink)}
  .brand .name{font-family:"Bebas Neue",sans-serif;line-height:1;letter-spacing:.5px}
  .brand .tag{font-family:"Montserrat",sans-serif;font-weight:300;letter-spacing:3px;text-transform:uppercase;color:#222}

  /* bottle label */
  .label{left:140px;top:440px;width:300px;height:400px}
  .label .top{position:absolute;inset:0 0 auto 0;height:190px;display:flex;flex-direction:column;justify-content:flex-end;padding-bottom:22px}
  .label .brand .name{font-size:44px}
  .label .brand .tag{font-size:11px}
  .label .band{position:absolute;left:0;right:0;top:190px;height:72px;background:var(--teal);display:flex;align-items:center;justify-content:center;color:#fff;font-size:50px;text-shadow:0 2px 0 rgba(0,0,0,.18)}
  .label .red{position:absolute;left:0;right:0;top:262px;bottom:0;background:var(--red)}

  .pill{background:#fff;color:var(--red);border-radius:0 0 12px 12px;font-family:"Montserrat",sans-serif;font-weight:500;text-align:center;margin:0 auto}
  .label .pill{width:200px;font-size:10.5px;padding:5px 0}
  .wild{font-family:"Montserrat",sans-serif;font-weight:300;color:#fff;text-align:center}
  .claim{font-family:"Montserrat",sans-serif;font-weight:700;color:#fff;text-align:center}
  .label .wild{font-size:12px;margin-top:14px}
  .label .claim{font-size:9.5px;margin-top:4px}
  .tri{position:absolute;left:50%;bottom:0;transform:translateX(-50%);background:#fff;clip-path:polygon(50% 0,100% 100%,0 100%);display:flex;align-items:flex-end;justify-content:center;color:#2a8b91;font-family:"Montserrat",sans-serif;font-weight:500}
  .label .tri{width:70px;height:40px;font-size:6px;padding-bottom:6px}

  /* box side */
  .side{left:500px;top:128px;width:180px;height:920px}
  .side .teal{position:absolute;inset:0 0 auto 0;height:320px;background:var(--teal);color:#fff;text-align:center;padding-top:100px}
  .side .wild{font-size:13px}
  .side .claim-c{font-family:"Bebas Neue",sans-serif;font-size:34px;line-height:1.05;margin-top:8px;color:#fff}
  .side .body{position:absolute;left:0;right:0;top:320px;bottom:14px;padding:0 16px}
  .side .brand{margin-top:140px}
  .side .brand .name{font-size:34px}
  .side .brand .tag{font-size:9px;letter-spacing:1.5px}
  .side h2{font-family:"Bebas Neue",sans-serif;font-weight:400;color:var(--red);font-size:22px;text-align:center;margin-top:36px}
  .side p{font-family:"Bebas Neue",sans-serif;font-size:12.5px;line-height:1.62;color:var(--ink);text-align:center;margin-top:12px;letter-spacing:.2px}
  .badges{display:flex;justify-content:space-between;margin-top:30px}
  .badges span{width:30px;height:40px;border-radius:50%;background:var(--badge)}
  .side .foot{position:absolute;left:0;right:0;bottom:0;height:14px;background:var(--teal)}

  /* box front */
  .front{left:680px;top:128px;width:340px;height:920px}
  .front .top{position:absolute;inset:0 0 auto 0;height:315px;display:flex;flex-direction:column;justify-content:flex-end;padding-bottom:42px}
  .front .brand .name{font-size:50px}
  .front .brand .tag{font-size:13px}
  .front .band{position:absolute;left:0;right:0;top:315px;height:190px;background:var(--teal);color:#fff;text-align:center;font-size:94px;line-height:.84;padding-top:20px;text-shadow:0 3px 0 rgba(0,0,0,.2)}
  .front .red{position:absolute;left:0;right:0;top:505px;bottom:0;background:var(--red)}
  .front .pill{width:228px;font-size:13.5px;padding:8px 0}
  .front .wild{font-size:16px;margin-top:46px}
  .front .claim{font-size:19px;line-height:1.4;margin-top:6px}
  .front .deco{position:absolute;left:0;right:0;bottom:0;height:230px;background:radial-gradient(ellipse at 50% 40%,#ee3b3f 0%,var(--red) 70%)}
  .front .tri{width:150px;height:92px;font-size:13px;padding-bottom:12px}
</style>
</head>
<body>
<div class="canvas">

  <section class="panel label" aria-label="Bottle label">
    <div class="top brand">
      <div class="name">Balm Vesper</div>
      <div class="tag">Skin and Body Care</div>
    </div>
    <div class="band condensed">Muscle and Joint</div>
    <div class="red">
      <div class="pill">MUSCLES ET ARTICULATIONS</div>
      <div class="wild">Made with Wildcrafted</div>
      <div class="claim">PURE ESSENTIAL OILS AND HEMP SEED OIL</div>
      <div class="tri">30ml/1fl.oz</div>
    </div>
  </section>

  <section class="panel side" aria-label="Box side panel">
    <div class="teal">
      <div class="wild">Made with Wildcrafted</div>
      <div class="claim-c">Pure Essential<br>Oils and Hemp<br>Seed Oil</div>
    </div>
    <div class="body">
      <div class="brand">
        <div class="name">Balm Vesper</div>
        <div class="tag">Skin and Body Care</div>
      </div>
      <h2>Directions</h2>
      <p>Lorem Ipsum is simply dummy text of the printing and typesetting industry. Lorem Ipsum has been the industry's standard dummy text ever since the 1500s, when an unknown printer took a galley of type and scrambled it to make a type specimen book. It has survived not only five centuries, but also the leap into electronic typesetting, remaining essentially unchanged.</p>
      <div class="badges" aria-label="Certification badges">
        <span></span><span></span><span></span><span></span>
      </div>
    </div>
    <div class="foot"></div>
  </section>

  <section class="panel front" aria-label="Box front panel">
    <div class="top brand">
      <div class="name">Balm Vesper</div>
      <div class="tag">Skin and Body Care</div>
    </div>
    <div class="band condensed">Muscle<br>and Joint</div>
    <div class="red">
      <div class="pill">MUSCLES ET ARTICULATIONS</div>
      <div class="wild">Made with Wildcrafted</div>
      <div class="claim">PURE ESSENTIAL OILS<br>AND HEMP SEED OIL</div>
      <div class="deco" role="img" aria-label="Large decorative red flower motif"></div>
      <div class="tri">30ml/1fl.oz</div>
    </div>
  </section>

</div>
</body>
</html>
```